Talvinor needs a Webpage Design

We need a webpage for Dr. XYZ who is doing consultancy practice in the area of speech, language, and reading disabilities. He is doing his consultancy practice as "Talvinor Consultants". Our target market is clients with annual income of $100,000 or more in Chicago area. Our business philosophy is: "...We provide the best evidence-based services/interventions, at an affordable fee, and deal only with clients who seek such services...."

Dr. XYZ's area of research interests are: a) using assistive technology for communication for children with autism, b) early intervention with focus on parent participation, and c) language learning for children birth-to-five years.

He works at a public university whose school color is 'Orange". Home page should show two logos (university and practice). Each page should stand on its own and reflect the content with minimal scrolling. The colors should be subdued (not bright colors) to attract college educated wealthy individuals who are seeking best evidence-based practice in speech, language, and reading for their children.

We need five pages: Home, Consultation, Research, Professional Development, and Contact (with google map directions). The home page should have space for a picture and links for facebook, twitter, and google plus. Other pages should have space for at least one picture and links to pdf files.

The overall design should show healthcare service, evidence-based early intervention with focus on parent participation, and project that we are leaders in the field.

```html
<!DOCTYPE html>
<html lang="en">
<head>
<meta charset="utf-8">
<title>Talvinor Consultants</title>
<link href="https://fonts.googleapis.com/css2?family=Mulish:wght@300;400;600&display=swap" rel="stylesheet">
<style>
:root{
  --blue:#1a78d8;
  --footer:#1b6fd6;
  --ink:#333;
  --text:#555;
  --grey-band:#f1f1f1;
  --rule:#c9c9c9;
  --white:#fff;
}
*{box-sizing:border-box;margin:0;padding:0}
html,body{width:814px;height:1200px;overflow:hidden;background:var(--white)}
body{position:relative;font-family:"Mulish",sans-serif;color:var(--ink)}
.abs{position:absolute}
.brand{left:88px;top:20px;width:146px;text-align:right}
.brand-name{font-size:26px;font-weight:600;color:var(--blue);line-height:1;text-align:left}
.brand-sub{font-size:17px;color:#555;margin-top:4px;line-height:1}
.doctor{left:378px;top:50px;font-size:17px;color:#222}
.doctor span{color:var(--blue)}
.email{left:88px;top:86px;font-size:12.5px;color:#222;display:flex;align-items:center;gap:6px}
.email a{color:var(--blue);text-decoration:none}
.nav{left:88px;top:126px;width:637px;height:34px;background:linear-gradient(#3a3a3a,#262626);display:flex}
.nav a{color:var(--white);font-size:10.5px;text-decoration:none;display:flex;align-items:center;justify-content:center;border-right:1px solid #444;letter-spacing:.2px}
.nav a:last-child{border-right:0}
.hero{left:88px;top:160px;width:637px;height:293px;background:linear-gradient(100deg,#e9e6df 0%,#d9d3c6 40%,#c9b99a 70%,#e2d2a6 100%)}
.hero-shadow{left:110px;top:452px;width:593px;height:12px;background:radial-gradient(ellipse at top,rgba(0,0,0,.28),transparent 70%)}
.hero-caption{left:88px;top:238px;width:418px;height:84px;background:rgba(255,255,255,.88);padding:4px 0 0 19px;font-size:21.5px;line-height:24.5px;color:var(--blue)}
.dots{left:380px;top:428px;display:flex;gap:6px}
.dots i{width:10px;height:10px;border-radius:50%;background:#222;display:block}
.center{left:88px;width:637px;text-align:center}
h2{font-weight:400;font-size:18px;color:#222;white-space:nowrap}
.sub-title{font-size:17px;top:951px}
.intro{top:521px;font-size:9.4px;line-height:15.6px;color:var(--text)}
.more{font-size:9.6px;color:var(--blue);text-decoration:none}
.bar{height:3px;background:var(--rule)}
.band{left:0;top:619px;width:814px;height:311px;background:var(--grey-band)}
.card{top:678px;width:203px;height:234px;background:var(--white);border:1px solid #e2e2e2;text-align:center}
.card-photo{margin:13px auto 0;width:180px;height:98px}
.card h3{font-size:12.5px;font-weight:400;color:var(--blue);margin-top:12px;letter-spacing:.2px;white-space:nowrap}
.card p{font-size:9px;line-height:15.5px;color:var(--text);margin-top:3px;padding:0 12px;letter-spacing:-.1px}
.card .more{display:block;margin-top:6px}
.card-shadow{top:910px;width:180px;height:8px;background:radial-gradient(ellipse at top,rgba(0,0,0,.22),transparent 70%)}
.research-photo{left:88px;top:990px;width:149px;height:102px;border:1px solid #ddd;background:linear-gradient(135deg,#f4f1ea,#d8cfbd 60%,#c9a95a)}
.updates{left:258px;top:988px;list-style:none;font-size:9.4px;line-height:13px;color:var(--text)}
.updates li{position:relative;padding-left:18px;margin-bottom:9px;width:250px}
.updates svg{position:absolute;left:2px;top:2px}
.pd-item{left:518px;width:207px;height:64px;border-bottom:1px solid #ddd;display:flex;gap:8px;padding:3px 0 0 3px}
.pd-photo{width:49px;height:49px;flex:none}
.pd-text{font-size:8px;line-height:11px;color:var(--text)}
.pd-text b{display:block;font-weight:400;color:var(--blue);margin-top:8px}
.footer{left:0;top:1126px;width:814px;height:74px;background:var(--footer);color:var(--white)}
.footer-links{left:88px;top:14px;font-size:9.3px}
.footer-links a{color:var(--white);text-decoration:none}
.footer-links span{margin:0 7px}
.copy{left:88px;top:42px;font-size:8px}
.connect{left:653px;top:14px;font-size:11px}
.social{left:653px;top:34px;display:flex;gap:4px}
.social a{width:22px;height:22px;border-radius:50%;background:var(--white);display:block}
</style>
</head>
<body>

<header>
  <div class="abs brand">
    <div class="brand-name">Talvinor</div>
    <div class="brand-sub">Consultants</div>
  </div>
  <div class="abs doctor"><span>Dr</span> XYZ</div>
  <div class="abs email">
    <svg width="14" height="10" viewBox="0 0 14 10"><rect x=".5" y=".5" width="13" height="9" fill="none" stroke="#555"/><path d="M.5 .5 7 6l6.5-5.5M.5 9.5 5 5m8.5 4.5L9 5" fill="none" stroke="#555"/></svg>
    Email : <a href="mailto:info@talvinor-consult.com">info@talvinor-consult.com</a>
  </div>
  <nav class="abs nav">
    <a href="#" style="width:86px">HOME</a>
    <a href="#" style="width:133px">CONSULTATION</a>
    <a href="#" style="width:106px">RESEARCH</a>
    <a href="#" style="width:209px">PROFESSIONAL DEVELOPMENT</a>
    <a href="#" style="width:103px">CONTACT</a>
  </nav>
</header>

<section>
  <div class="abs hero" role="img" aria-label="Therapist working with a young girl in a bright playroom"></div>
  <div class="abs hero-shadow"></div>
  <p class="abs hero-caption">We are doing consultancy practice in the area of speech, language, and reading disabilities.</p>
  <div class="abs dots"><i></i><i></i><i></i><i></i></div>
</section>

<section>
  <h2 class="abs center" style="top:486px">Welcome to Our Website</h2>
  <p class="abs center intro">Lorem ipsum dolor sit amet, consect- etuer adipiscing elit, sed diam nonummy nibh euismod tincidunt ut laoreet dolore magna aliquam erat volutpat. Ut wisi enim ad minim veniam, quis nostrud exerci tation ullam. Consectetuer adipiscing elit, sed diam nonummy nibh euismod tincidunt ut laoreet dolore magna aliquam erat volut- pat. Ut wisi enim ad minim veniam, quis nostrud exerci tation ullam.</p>
  <a class="abs center more" style="top:583px" href="#">READ MORE ››</a>
  <div class="abs bar" style="left:353px;top:600px;width:108px"></div>
</section>

<section>
  <div class="abs band"></div>
  <h2 class="abs center" style="top:638px">What We Do</h2>

  <article class="abs card" style="left:88px">
    <div class="card-photo" role="img" aria-label="Child using a tablet with an adult" style="background:linear-gradient(135deg,#6b5a2e,#8c7a45 50%,#c9b8a0)"></div>
    <h3>ASSISTIVE TECHNOLOGY</h3>
    <p>Lorem ipsum dolor sit amet, consect- etuer adipiscing elit, sed diam nonummy nibh euismod tincidunt ut laoreet dolore magna...</p>
    <a class="more" href="#">Learn More ››</a>
  </article>
  <article class="abs card" style="left:306px">
    <div class="card-photo" role="img" aria-label="Young boy and a woman talking together" style="background:linear-gradient(90deg,#f1ece6,#e3c9b5 45%,#5a3a2c 80%,#2e2a28)"></div>
    <h3>EARLY LANGUAGE LEARNING</h3>
    <p>Lorem ipsum dolor sit amet, consect- etuer adipiscing elit, sed diam nonummy nibh euismod tincidunt ut laoreet dolore magna...</p>
    <a class="more" href="#">Learn More ››</a>
  </article>
  <article class="abs card" style="left:522px">
    <div class="card-photo" role="img" aria-label="Father reading a book with his son" style="background:linear-gradient(90deg,#d9d5cf,#4a5570 35%,#d8c2ac 65%,#ecebe8)"></div>
    <h3>READING DIFFICULTIES</h3>
    <p>Lorem ipsum dolor sit amet, consect- etuer adipiscing elit, sed diam nonummy nibh euismod tincidunt ut laoreet dolore magna...</p>
    <a class="more" href="#">Learn More ››</a>
  </article>
  <div class="abs card-shadow" style="left:100px"></div>
  <div class="abs card-shadow" style="left:318px"></div>
  <div class="abs card-shadow" style="left:534px"></div>
</section>

<section>
  <h2 class="abs sub-title" style="left:88px">Research Updates 365</h2>
  <div class="abs research-photo" role="img" aria-label="Fountain pen resting on a dictionary entry"></div>
  <ul class="abs updates">
    <li><svg width="9" height="8" viewBox="0 0 9 8"><path d="M1 4l2.5 2.5L8 1" fill="none" stroke="#1a78d8" stroke-width="1.8"/></svg>Using assistive technology for communication for children with autism..</li>
    <li><svg width="9" height="8" viewBox="0 0 9 8"><path d="M1 4l2.5 2.5L8 1" fill="none" stroke="#1a78d8" stroke-width="1.8"/></svg>Early intervention with focus on parent participation</li>
    <li><svg width="9" height="8" viewBox="0 0 9 8"><path d="M1 4l2.5 2.5L8 1" fill="none" stroke="#1a78d8" stroke-width="1.8"/></svg>Language learning for children birth-to-five years</li>
  </ul>
  <a class="abs more" style="left:258px;top:1075px" href="#">READ MORE ››</a>
  <div class="abs bar" style="left:258px;top:1090px;width:109px"></div>
</section>

<section>
  <h2 class="abs sub-title" style="right:89px">Professional development</h2>
  <div class="abs pd-item" style="top:985px">
    <div class="pd-photo" role="img" aria-label="Speaker presenting to a seminar audience" style="background:linear-gradient(135deg,#e8ecef,#7a8796 60%,#2f3a48)"></div>
    <p class="pd-text">Lorem ipsum dolor sit amet, consect- etuer adipiscing elit, sed di nonummy tincidunt ut laoreet dolore magna<b>-MARA</b></p>
  </div>
  <div class="abs pd-item" style="top:1049px">
    <div class="pd-photo" role="img" aria-label="Group of professionals in business attire" style="background:linear-gradient(135deg,#eef0f2,#9aa2ab 55%,#2b2e35)"></div>
    <p class="pd-text">Lorem ipsum dolor sit amet, consect- etuer adipiscing elit, sed di nonummy tincidunt ut laoreet dolore magna<b>-MARA</b></p>
  </div>
</section>

<footer class="abs footer">
  <div class="abs footer-links"><a href="#">Home</a><span>/</span><a href="#">Consultation</a><span>/</span><a href="#">Research</a><span>/</span><a href="#">Professional Development</a><span>/</span><a href="#">Contact</a></div>
  <div class="abs copy">Copyright © 2014. Talvinor Consultants. All Right Reserved</div>
  <div class="abs connect">Connect Us:</div>
  <div class="abs social">
    <a href="#" aria-label="Social profile one"></a>
    <a href="#" aria-label="Social profile two"></a>
    <a href="#" aria-label="Social profile three"></a>
  </div>
</footer>

</body>
</html>
```